Lorvik.no is a new website about pedagogical entrepreneurship. It's main target group is teachers. The Fjellmark Bureau for Digital Schooling and the Halvstad Agency for Classroom Affairs are leading the project.

The web page is meant to show examples of how different methods of entrepreneurship can be used pedagogical in a learning environment. The page will also support the user with examples of different teaching programs and other examples of best practice.

Pedagogical entrepreneurship is not about business and men in suits. It's a method for learning. The focus in the design should be on school, education and new ways of learning.

The final product should be motivating and engaging, but at the same time governmental and serious. We are not looking for something "flashy" and corporate-looking, but a moderate, task-focused and clean design that state quality.

We need designs for three pages:
1 - frontpage
2 - subpage ("Metoder og undervisningsopplegg")
3 - subpage ("Tavle-KOMP i Brekkvoll")

The interaction design for these three pages will be uploaded as an attachment.

We would like you to find inspiration in the following websites:
- www.skaperlund.no
- www.guldrim.no
- www.brambelquest.com
- www.tuv.no
(more will be added)

Please use the attached logo, and feel free to use this as an inspiration for the rest of the design.

Reason: We are awaiting improved designs from some designers, and need to extend the deadline a couple of days.

Target Market(s)

Teachers

Industry/Entity Type

Education

Requirements
Must have
• * Header with: Logo. Main navigation. Utility navigation. Search box.
* Footer
Should not have
• Images of men in suits.
Very strong graphical elements that stands out too much (we want it clean).

```html
<!DOCTYPE html>
<html lang="en">
<head>
<meta charset="utf-8">
<title>Lorvik.no – Methods &amp; Teaching Plans</title>
<link href="https://fonts.googleapis.com/css2?family=Oswald:wght@400;500&family=Pathway+Gothic+One&family=Arimo:wght@400&family=Open+Sans:wght@400;700&display=swap" rel="stylesheet">
<style>
:root{
  --header-top:#052a4d;
  --header-mid:#0a4f86;
  --header-bottom:#0b7ac0;
  --tab:#5bbdec;
  --tab-light:#7fcdf2;
  --bar-blue:#0a6fae;
  --bar-blue-dark:#075a92;
  --bar-dark:#444444;
  --circle:#4ab8ec;
  --circle-active:#333333;
  --link-blue:#0f6fae;
  --text:#333333;
  --muted:#555555;
  --line:#cfcfcf;
  --footer:#333333;
  --footer-text:#bdbdbd;
  --footer-head:#d8d8d8;
  --pill:#b9b9b9;
  --white:#ffffff;
}
*{box-sizing:border-box;margin:0;padding:0}
html,body{width:1000px;height:1200px;overflow:hidden}
body{position:relative;background:var(--white);font-family:"Arimo",Arial,sans-serif;color:var(--text)}
a{color:inherit;text-decoration:none}
ul{list-style:none}

/* header */
.site-header{position:absolute;left:0;top:0;width:1000px;height:241px;
  background:linear-gradient(180deg,var(--header-top) 0%,var(--header-mid) 45%,var(--header-bottom) 100%)}
.brand{position:absolute;left:22px;top:56px;display:flex;align-items:center;gap:26px}
.brand-mark{width:72px;height:72px;border-radius:50%;background:var(--tab)}
.brand-name{font-family:"Open Sans",sans-serif;font-weight:700;font-size:50px;line-height:1;color:var(--tab);letter-spacing:-1px}
.brand-tagline{position:absolute;left:122px;top:114px;font-family:"Open Sans",sans-serif;font-size:10.5px;color:var(--white)}
.utility-nav{position:absolute;right:62px;top:32px;display:flex;gap:14px;font-family:"Open Sans",sans-serif;font-size:13.5px;color:#8fd3f7}
.utility-nav .sep{color:#8fd3f7}
.search{position:absolute;left:640px;top:82px;width:270px;height:31px;background:#e8eef2;border:1px solid #b7c7d3;
  font-family:"Open Sans",sans-serif;font-style:italic;font-size:13px;color:#6a8aa4;padding:6px 12px}
.search-button{position:absolute;left:913px;top:84px;width:28px;height:28px;border-radius:50%;
  background:linear-gradient(#ffffff,#cfd6dc);box-shadow:0 1px 3px rgba(0,0,0,.5)}
.search-button svg{position:absolute;left:6px;top:6px}
.main-nav{position:absolute;left:0;top:183px;width:1000px;height:58px}
.main-nav a{position:absolute;top:0;height:58px;border-radius:16px 16px 0 0;
  background:linear-gradient(var(--tab-light),var(--tab));
  font-family:"Pathway Gothic One",sans-serif;font-size:31px;color:var(--white);text-align:center;line-height:62px}
.tab-1{left:21px;width:316px}
.tab-2{left:344px;width:316px}
.tab-3{left:667px;width:317px}

/* section bars */
.section-bar{position:absolute;left:24px;width:948px;height:39px;border-radius:4px;
  font-family:"Oswald",sans-serif;font-weight:500;font-size:19px;color:var(--white);padding-left:30px;line-height:39px}
.section-bar::before{content:"";position:absolute;left:9px;top:13px;width:13px;height:13px;border-radius:50%;background:var(--white)}
.section-bar::after{content:"";position:absolute;left:13px;top:17px;width:5px;height:5px;border-top:1.5px solid #333;border-right:1.5px solid #333;transform:rotate(45deg)}
.bar-methods{top:258px;background:linear-gradient(var(--bar-blue),var(--bar-blue-dark))}
.bar-plans{top:544px;background:var(--bar-dark)}

/* methods */
.methods-list{position:absolute;left:25px;top:308px;width:653px;height:214px;border:1px solid var(--line)}
.method{position:absolute;display:flex;align-items:center;gap:14px;font-size:15.5px;color:var(--text)}
.method-num{width:39px;height:39px;border-radius:50%;background:var(--circle);color:var(--white);
  font-family:"Oswald",sans-serif;font-size:21px;text-align:center;line-height:39px}
.method.is-active .method-num{background:var(--circle-active)}
.method.is-active .method-name{color:var(--link-blue)}
.method-quote{position:absolute;left:690px;top:320px;width:280px;height:190px}
.quote-mark{position:absolute;font-family:Georgia,serif;font-size:44px;font-weight:700;color:#b5b5b5;line-height:1}
.quote-open{left:0;top:0}
.quote-close{right:4px;top:158px}
.quote-title{position:absolute;left:48px;top:28px;font-size:15px;color:var(--link-blue)}
.quote-text{position:absolute;left:12px;top:59px;width:252px;font-size:12.6px;line-height:16.3px;color:#222;text-align:justify}

/* teaching plans table */
.plans{position:absolute;left:25px;top:592px;width:947px;height:380px;border:1px solid var(--line);border-top:none;overflow:hidden}
.plans-head{position:absolute;left:0;top:0;width:947px;height:57px;background:linear-gradient(var(--bar-blue),var(--bar-blue-dark));
  font-size:14.5px;color:var(--white)}
.plans-head span,.plan-row span{position:absolute}
.plans-head span{top:20px}
.plan-row{position:absolute;left:0;width:947px;height:45px;border-bottom:1px dotted #555;font-size:13.8px;color:#111}
.plan-row:last-child{border-bottom:none}
.plan-row span{top:15px}
.c-no{left:29px}.c-title{left:84px}.c-level{left:279px}.c-time{left:527px}.c-subject{left:726px}
.plans-head .c-no{left:21px}.plans-head .c-time{left:526px}.plans-head .c-subject{left:729px}
.scrollbar{position:absolute;left:934px;top:61px;width:7px;height:204px;border-radius:4px;background:#8a8a8a}

/* footer */
.site-footer{position:absolute;left:0;top:983px;width:1000px;height:217px;background:var(--footer);font-family:"Open Sans",sans-serif}
.footer-col{position:absolute;top:35px}
.footer-col h3{font-family:"Oswald",sans-serif;font-weight:400;font-size:14px;color:var(--footer-head);margin-bottom:13px;letter-spacing:.2px}
.footer-col li{font-size:12.3px;line-height:17px;color:var(--footer-text)}
.see-more{display:inline-block;margin-top:9px;height:21px;padding:0 7px 0 6px;border-radius:11px;background:var(--pill);
  font-family:"Oswald",sans-serif;font-size:11.5px;line-height:21px;color:#333}
.col-about{left:25px;width:200px}
.col-about .see-more{position:absolute;left:-2px;top:143px;margin:0}
.col-methods{left:265px}
.col-plans{left:415px}
.col-examples{left:575px}
.footer-divider{position:absolute;left:780px;top:32px;width:1px;height:128px;background:#555}
.social{position:absolute;left:806px;top:28px;display:flex;gap:11px}
.social li{width:33px;height:33px;border-radius:4px;background:linear-gradient(#8a8a8a,#5e5e5e)}
.footer-brand{position:absolute;left:858px;top:88px;width:70px;height:70px;border-radius:50%;background:#9a9a9a}
.footer-legal{position:absolute;left:780px;top:178px;width:222px;text-align:center;font-size:11.3px;line-height:16px;color:#cfcfcf}
</style>
</head>
<body>

<header class="site-header">
  <div class="brand">
    <span class="brand-mark"></span>
    <span class="brand-name">Lorvik</span>
  </div>
  <div class="brand-tagline">Entreprenørielle metoder i undervisningen</div>

  <nav class="utility-nav">
    <a href="#">Best Practice Schools</a><span class="sep">|</span>
    <a href="#">Lorvikmeter</a><span class="sep">|</span>
    <a href="#">About Lorvik.no</a>
  </nav>

  <div class="search">Search Here</div>
  <div class="search-button">
    <svg width="16" height="16" viewBox="0 0 16 16" aria-hidden="true">
      <circle cx="6" cy="6" r="4" fill="none" stroke="#222" stroke-width="2"/>
      <line x1="9" y1="9" x2="14" y2="14" stroke="#222" stroke-width="2.5" stroke-linecap="round"/>
    </svg>
  </div>

  <nav class="main-nav">
    <a class="tab-1" href="#">Pedagogical Entrepreneurship</a>
    <a class="tab-2" href="#">Methods &amp; Teaching Plans</a>
    <a class="tab-3" href="#">Good Examples / Best Practices</a>
  </nav>
</header>

<h2 class="section-bar bar-methods">METHODS</h2>

<section class="methods-list">
  <div class="method" style="left:8px;top:15px"><span class="method-num">01</span><span class="method-name">Story Line</span></div>
  <div class="method is-active" style="left:8px;top:85px"><span class="method-num">02</span><span class="method-name">Elevbedrift/ungdomsbedrift</span></div>
  <div class="method" style="left:8px;top:155px"><span class="method-num">03</span><span class="method-name">Problembasert laering</span></div>
  <div class="method" style="left:251px;top:15px"><span class="method-num">04</span><span class="method-name">Real</span></div>
  <div class="method" style="left:251px;top:85px"><span class="method-num">05</span><span class="method-name">Uteskole-pedagogikk</span></div>
  <div class="method" style="left:251px;top:155px"><span class="method-num">06</span><span class="method-name">Partnerskap</span></div>
  <div class="method" style="left:458px;top:15px"><span class="method-num">07</span><span class="method-name">Prosjektarbeid</span></div>
  <div class="method" style="left:458px;top:85px"><span class="method-num">08</span><span class="method-name">Kreative ekskursjoner</span></div>
  <div class="method" style="left:458px;top:155px"><span class="method-num">09</span><span class="method-name">Grundercamp</span></div>
</section>

<aside class="method-quote">
  <span class="quote-mark quote-open">“</span>
  <h3 class="quote-title">Elevbedrift/ungdomsbedrift</h3>
  <p class="quote-text">Lorem ipsum dolor sit amet, consectetur adipisicing elit, sed do eiusmod tempor incididunt ut labore et dolore magna aliqua. Ut enim ad minim veniam, quis nostrud exercitation ullamco laboris nisi ut aliquip ex ea commodo consequat.</p>
  <span class="quote-mark quote-close">”</span>
</aside>

<h2 class="section-bar bar-plans">FIND TEACHING PLANS</h2>

<section class="plans">
  <div class="plans-head">
    <span class="c-no">S.NO</span><span class="c-title">TITLE</span><span class="c-level">CLASS/LEVEL</span><span class="c-time">TIME</span><span class="c-subject">SUBJECT</span>
  </div>
  <div class="plan-rows">
    <div class="plan-row" style="top:59px"><span class="c-no">01.</span><span class="c-title">Lorem Ipsum</span><span class="c-level">5 -7 Level</span><span class="c-time">05:00</span><span class="c-subject">Norwegian, English, Mathematics</span></div>
    <div class="plan-row" style="top:104px"><span class="c-no">02.</span><span class="c-title">Lorem Ipsum</span><span class="c-level">5 -7 Level</span><span class="c-time">05:00</span><span class="c-subject">Norwegian, English, Mathematics</span></div>
    <div class="plan-row" style="top:149px"><span class="c-no">03.</span><span class="c-title">Lorem Ipsum</span><span class="c-level">5 -7 Level</span><span class="c-time">05:00</span><span class="c-subject">Norwegian, English, Mathematics</span></div>
    <div class="plan-row" style="top:194px"><span class="c-no">04.</span><span class="c-title">Lorem Ipsum</span><span class="c-level">5 -7 Level</span><span class="c-time">05:00</span><span class="c-subject">Norwegian, English, Mathematics</span></div>
    <div class="plan-row" style="top:239px"><span class="c-no">05.</span><span class="c-title">Lorem Ipsum</span><span class="c-level">5 -7 Level</span><span class="c-time">05:00</span><span class="c-subject">Norwegian, English, Mathematics</span></div>
    <div class="plan-row" style="top:284px"><span class="c-no">06.</span><span class="c-title">Lorem Ipsum</span><span class="c-level">5 -7 Level</span><span class="c-time">05:00</span><span class="c-subject">Norwegian, English, Mathematics</span></div>
    <div class="plan-row" style="top:329px;border-bottom:none"><span class="c-no">07.</span><span class="c-title">Lorem Ipsum</span><span class="c-level">5 -7 Level</span><span class="c-time">05:00</span><span class="c-subject">Norwegian, English, Mathematics</span></div>
  </div>
  <div class="scrollbar"></div>
</section>

<footer class="site-footer">
  <div class="footer-col col-about">
    <h3>PEDAGOGICAL ENTREPRENEURSHIP</h3>
    <ul>
      <li>What is pedagogical<br>entrepreneurship?</li>
      <li>Science</li>
      <li>Best Practice Schools</li>
      <li>Lorvikmeter</li>
      <li>About Lorvik.no</li>
    </ul>
    <a class="see-more" href="#">SEE MORE →</a>
  </div>
  <div class="footer-col col-methods">
    <h3>METHODS</h3>
    <ul><li>Story line</li><li>REAL</li><li>Cafe-pedagogikk</li></ul>
    <a class="see-more" href="#">SEE MORE →</a>
  </div>
  <div class="footer-col col-plans">
    <h3>TEACHING PLANS</h3>
    <ul><li>Teaching Plan 1</li><li>Teaching Plan 2</li><li>Teaching Plan 3</li><li>Teaching Plan 4</li></ul>
    <a class="see-more" href="#">SEE MORE →</a>
  </div>
  <div class="footer-col col-examples">
    <h3>GOOD EXAMPLES</h3>
    <ul>
      <li>Tavle-KOMP at Brekkvoll School</li>
      <li>Tavle-KOMP at Brekkvoll School</li>
      <li>Tavle-KOMP at Brekkvoll School</li>
      <li>Tavle-KOMP at Brekkvoll School</li>
      <li>Tavle-KOMP at Brekkvoll School</li>
    </ul>
    <a class="see-more" href="#">SEE MORE →</a>
  </div>
  <div class="footer-divider"></div>
  <ul class="social" aria-label="Social links"><li></li><li></li><li></li><li></li></ul>
  <div class="footer-brand" aria-hidden="true"></div>
  <p class="footer-legal">Lorvik.no<br>Copyrights 2012.All Rights Reserved.</p>
</footer>

</body>
</html>
```